Corporate Intelligence Agency seeks redesign *

Brightfen Advisory is a business intelligence firm made up of former special operations and intelligence professionals. Our vibe is quiet professionals that get the job done by whatever means necessary.
Our aesthetic is clean, sleek, and monochromatic. We prefer the texture contrasts over colors. Slick white or black, playing up textures, and bold block lettering, and simplicity are what we are looking for in a design.

The logo would preferably pay homage to our military/special operations roots, and the culture of changing for the better (alchemy) that we embody all while remaining simple.

Target Market(s)

C-Level executives with a taste for the simple over the extravagant, and cut right to the chase

Industry/Entity Type

Management Solution

Contact Information for Business Card

Back is matte black with a glossy black logo to contrast. The front has the logo, with space on the bottom left for name and contact

Logo Text

Brightfen Adv.

Logo styles of interest
Abstract Logo
Wordmark Logo
Lettermark Logo
Font styles to use
Serif
Sans Serif
Script

Requirements
Must have
• Monochromatic, play on texture within card (the card ought to be memorable to hold), solid/clean lettering. Logo should be simple and sleek.
Nice to have
• If the logo can tie alchemy and intelligence/spy genre. 3d textures
Should not have
• Nothing overtly military. No colors outside of the monochromatic spectrum

```html
<!DOCTYPE html>
<html lang="en">
<head>
<meta charset="utf-8">
<title>Brightfen Advisory – Business Cards</title>
<link rel="stylesheet" href="https://fonts.googleapis.com/css2?family=Open+Sans:wght@400;600;700&display=swap">
<style>
  :root {
    --backdrop: #2b2d2e;
    --card: #050505;
    --card-edge: #1a1a1a;
    --silver: #c9c9c9;
    --silver-soft: #a8a8a8;
  }
  * { margin: 0; padding: 0; box-sizing: border-box; }
  html, body { width: 1200px; height: 892px; overflow: hidden; }
  body {
    background: var(--backdrop);
    font-family: "Open Sans", sans-serif;
    position: relative;
  }
  .card {
    position: absolute;
    width: 520px;
    height: 297px;
    background: var(--card);
    border: 1px solid var(--card-edge);
    box-shadow: 0 18px 40px rgba(0,0,0,.45);
  }
  .card--front { left: 50px; top: 298px; }
  .card--back  { left: 630px; top: 298px; }

  .wordmark {
    position: absolute;
    display: flex;
    align-items: center;
    gap: 12px;
    color: var(--silver);
    font-weight: 600;
    letter-spacing: .08em;
    text-transform: uppercase;
    white-space: nowrap;
  }
  .wordmark__square {
    width: 14px; height: 14px;
    background: var(--silver);
  }
  .card--back .wordmark {
    left: 50%; top: 50%;
    transform: translate(-50%, -50%);
    font-size: 30px;
  }
  .card--front .wordmark {
    right: 48px; top: 60px;
    font-size: 24px;
  }

  .person {
    position: absolute;
    right: 48px; top: 116px;
    text-align: right;
    color: var(--silver);
  }
  .person__name { font-size: 19px; font-weight: 700; }
  .person__title { font-size: 12px; color: var(--silver-soft); }

  .contact {
    position: absolute;
    left: 36px; bottom: 34px;
    color: var(--silver-soft);
    font-size: 12.5px;
    line-height: 1.9;
  }
  .contact__row span + span::before {
    content: "|";
    margin: 0 10px;
  }
</style>
</head>
<body>
  <section class="card card--front" aria-label="Business card front">
    <div class="wordmark"><span class="wordmark__square"></span><span>Brightfen Adv.</span></div>
    <div class="person">
      <p class="person__name">Mara Quill</p>
      <p class="person__title">Director</p>
    </div>
    <div class="contact">
      <p class="contact__row"><span>+61 400 555 013</span><span>48 Larch Street, NTH, 318</span></p>
      <p class="contact__row"><span>info@brightfen.com</span><span>www.brightfenadvisory.com</span></p>
    </div>
  </section>

  <section class="card card--back" aria-label="Business card back">
    <div class="wordmark"><span class="wordmark__square"></span><span>Brightfen Adv.</span></div>
  </section>
</body>
</html>
```